Marlow Vale Brewery website design,

I would like a website designed for my microbrewery, with a part that you can purchase beers from, links to our social media. The brand is luxury, old English, classic, timeless, simple, crisp and clean. I’d like to send you a design we have for the beer can so you can get understanding of what we are trying to achieve.

Please have a look at our Instagram and Facebook to get an understanding of what we are about.

Thank you.

Ned

Target Market(s)

Non beardy beer drinkers. Young, professional, seeking experiences and something to remember.

Industry/Entity Type

Brewery

Font styles to use
Other font styles liked:
• I will upload photos of what I’d like.

Colors

Designer to choose colors to be used in the design.

Requirements
Must have
• Photos of our beers, it must be a beautiful website, landing page video background of a beer slowly being poured into a glass.
Nice to have
• Shots of hops, grain, videos of steam from the brewing process.

```html
<!DOCTYPE html>
<html lang="en">
<head>
<meta charset="utf-8">
<title>Marlow Vale Brewery</title>
<link rel="stylesheet" href="https://fonts.googleapis.com/css2?family=Dancing+Script:wght@500;700&family=Open+Sans:wght@400;600&family=Oswald:wght@400&display=swap">
<style>
:root{
  --black:#050505;
  --ink:#0d0d0d;
  --panel:#232323;
  --tab:#2a2a2a;
  --gold:#c9a45c;
  --gold-deep:#b38f4b;
  --white:#ffffff;
  --muted:#cfcfcf;
  --line:#3a3a3a;
}
*{box-sizing:border-box;margin:0;padding:0}
html,body{width:1200px;height:3163px;overflow:hidden;background:var(--black)}
body{position:relative;font-family:"Open Sans",Arial,sans-serif;color:var(--white)}
.abs{position:absolute}
.script{font-family:"Dancing Script",cursive}
.brandmark{font-family:"Open Sans",Arial,sans-serif;font-weight:600;color:var(--gold);letter-spacing:2px}

/* header */
.site-header{left:0;top:0;width:1200px;height:89px;background:var(--black);border-bottom:1px solid #1c1c1c;z-index:5}
.tagline{left:90px;top:10px;font-size:11px;color:var(--muted);display:flex;align-items:center;gap:8px}
.tagline i{width:9px;height:9px;border:2px solid var(--gold);border-radius:50%;display:block}
.follow{right:90px;top:9px;font-size:11px;color:var(--muted);display:flex;align-items:center;gap:10px}
.follow span.sq{width:10px;height:10px;background:var(--muted);display:block}
.nav{top:52px;font-size:11px;color:var(--muted);letter-spacing:.5px}
.nav a{position:absolute;white-space:nowrap;color:var(--muted);text-decoration:none}
.logo-cap{left:500px;top:0;width:232px;height:154px;background:var(--black);border-radius:0 0 116px 116px;border-bottom:2px solid var(--gold-deep);z-index:6;display:flex;align-items:center;justify-content:center}
.logo-cap .brandmark{font-size:46px}

/* hero */
.hero{left:0;top:89px;width:1200px;height:533px;background:linear-gradient(100deg,#1a1a1a,#4a4a4a 45%,#2a2a2a 70%,#111)}
.hero-can{left:53px;top:80px;width:200px;height:390px;border-radius:18px 18px 10px 10px;background:linear-gradient(90deg,#0b0b0b,#262626 50%,#0b0b0b);border-top:26px solid #c8a24f}
.hero-copy{left:200px;top:168px;width:780px;text-align:center}
.hero-copy h1{font-family:"Oswald",sans-serif;font-weight:400;font-size:24px;line-height:25px;text-transform:uppercase;text-shadow:0 1px 3px #000}
.hero-copy .brand{font-size:34px;color:var(--gold);margin-top:8px}
.hero-copy .by{font-size:24px;margin-top:10px;font-weight:700}
.dots{left:566px;top:451px;display:flex;gap:9px}
.dots i{width:8px;height:8px;border-radius:50%;background:#fff;display:block}
.dots i:first-child{background:var(--gold)}
.arrow{top:255px}

/* welcome */
.divider{left:0;top:622px;width:1200px;height:6px;background:#f2f2f2}
.welcome{left:0;top:628px;width:1200px;height:349px;background:linear-gradient(180deg,#1b1b1b,#0e0e0e)}
.welcome .hello{left:93px;top:48px;font-size:44px;color:var(--gold);font-weight:700}
.welcome h2{left:93px;top:110px;font-size:25px;font-weight:400;letter-spacing:.3px}
.welcome p{left:93px;top:152px;width:480px;font-size:12px;line-height:22px;color:var(--muted)}
.mug{left:685px;top:15px;width:490px;height:274px;background:linear-gradient(90deg,#e5b53a 0 25%,#e9c9a6 40%,#f0d5bb);border-radius:10px 60px 60px 10px}

/* news */
.news{left:0;top:977px;width:1200px;height:620px;background:var(--black)}
.card{background:var(--panel);text-align:center}
.card .photo{width:100%;height:215px}
.card p{font-size:12px;line-height:22px;color:var(--muted);padding:0 20px}
.card h3{font-size:19px;font-weight:400;margin:24px 0 8px;letter-spacing:.5px}
.card .meta{position:absolute;left:0;bottom:0;width:100%;height:47px;background:var(--gold-deep);display:flex;justify-content:center;align-items:center;gap:22px;font-size:11px;color:#fff}
.card .meta span{display:flex;align-items:center;gap:5px}
.brand-block{left:440px;top:165px;width:320px;text-align:center}
.brand-block .name{font-family:"Open Sans",Arial,sans-serif;font-weight:600;color:var(--gold);font-size:29px;letter-spacing:7px;line-height:44px}
.brand-mono{left:520px;top:370px;width:160px;text-align:center;font-size:40px}

/* beers */
.can-strip{left:0;top:1597px;width:1200px;height:69px;background:linear-gradient(180deg,#0c1328,#1d2540 50%,#0c1328)}
.tabs{left:0;top:1672px;width:1200px;height:85px;background:var(--tab);display:flex}
.tabs div{flex:1;display:flex;align-items:center;justify-content:center;text-align:center;font-size:16px;line-height:22px;text-transform:uppercase;color:var(--muted);border-right:2px solid #555}
.tabs div:last-child{border-right:0}
.tabs .on{color:var(--gold)}

/* contact */
.contact{left:0;top:1782px;width:1200px;height:511px;background:linear-gradient(90deg,#000 0 55%,#1a1a1a 70%,#3a3a3a)}
.glass{left:21px;top:53px;width:380px;height:400px;background:radial-gradient(ellipse at 50% 55%,#c9c9c9,#6a6a6a 45%,#000 75%)}
.portrait{left:759px;top:0;width:441px;height:511px;background:linear-gradient(90deg,#111,#5b5b5b 45%,#2a2a2a)}
.contact h2{left:405px;top:95px;font-size:84px;font-weight:500;line-height:1}
.contact .info{left:312px;top:267px;font-size:15px;line-height:20px;text-align:right}
.ring{width:64px;height:64px;border:2px solid #fff;border-radius:50%;display:flex;align-items:center;justify-content:center;background:#000}
.contact .addr{left:604px;top:336px;font-size:15px;line-height:20px}

/* gallery */
.gallery{left:0;top:2293px;width:1200px;height:154px;display:flex}
.gallery div{flex:1}

/* updates */
.updates{left:0;top:2447px;width:1200px;height:210px;background:var(--black)}
.updates .kick{left:93px;top:62px;font-size:26px;color:var(--gold)}
.updates h2{left:93px;top:92px;font-size:30px;font-weight:400}
.field{left:605px;top:88px;width:371px;height:42px;border:1px solid var(--gold-deep)}
.subscribe{left:976px;top:88px;width:117px;height:42px;background:var(--gold-deep);color:#222;font-size:13px;display:flex;align-items:center;justify-content:center;letter-spacing:.5px}

/* footer */
.footer{left:0;top:2657px;width:1200px;height:506px;background:linear-gradient(180deg,#050505 0 55%,#1a120b 80%,#2c1d10)}
.footer-logo{left:488px;top:40px;width:224px;height:140px;border-bottom:2px solid var(--gold-deep);border-radius:0 0 112px 112px;display:flex;align-items:center;justify-content:center}
.footer-logo .brandmark{font-size:52px}
.col{top:254px;width:360px;text-align:center}
.col h4{font-size:20px;font-weight:400}
.col p{color:var(--gold);font-size:19px;line-height:28px;margin-top:2px}
.social{top:401px;width:44px;height:44px;background:var(--gold-deep)}
</style>
</head>
<body>

<header class="abs site-header">
  <div class="abs tagline"><i></i>Approved &amp; Originality</div>
  <div class="abs follow">Follow us <span class="sq"></span><span class="sq"></span><span class="sq"></span></div>
  <nav class="abs nav" style="left:0;width:1200px">
    <a style="left:229px">HOME</a>
    <a style="left:316px">ABOUT</a>
    <a style="left:424px">MENU</a>
    <a style="left:731px">SHOP</a>
    <a style="left:815px">BLOG</a>
    <a style="left:900px">CONTACT</a>
  </nav>
  <svg class="abs" style="left:1034px;top:52px" width="14" height="14" viewBox="0 0 14 14"><circle cx="6" cy="6" r="4.5" fill="none" stroke="#c9a45c" stroke-width="2"/><line x1="9.5" y1="9.5" x2="13" y2="13" stroke="#c9a45c" stroke-width="2"/></svg>
  <svg class="abs" style="left:1079px;top:53px" width="14" height="12" viewBox="0 0 14 12"><rect y="0" width="14" height="2" fill="#c9a45c"/><rect y="5" width="14" height="2" fill="#c9a45c"/><rect y="10" width="14" height="2" fill="#c9a45c"/></svg>
</header>
<div class="abs logo-cap"><span class="brandmark">MVB</span></div>

<section class="abs hero" role="img" aria-label="Monochrome photo of a traditional pub bar interior with stools">
  <div class="abs hero-can" role="img" aria-label="Black porter can with gold lid"></div>
  <div class="abs hero-copy">
    <h1>Some say, the ingredients for this porter are extracted from<br>hens teeth found only in the lair of a mystical unicorn</h1>
    <div class="script brand">Marlow Vale Brewery</div>
    <div class="script by">Some Friends Saya</div>
  </div>
  <div class="abs dots"><i></i><i></i><i></i></div>
  <svg class="abs arrow" style="left:12px" width="10" height="16" viewBox="0 0 10 16"><path d="M8 2 2 8l6 6" fill="none" stroke="#ccc" stroke-width="2"/></svg>
  <svg class="abs arrow" style="left:1166px" width="10" height="16" viewBox="0 0 10 16"><path d="M2 2l6 6-6 6" fill="none" stroke="#ccc" stroke-width="2"/></svg>
</section>

<div class="abs divider"></div>
<section class="abs welcome">
  <div class="abs script hello">Welcome!</div>
  <h2 class="abs">MAKING THE BEST BEER POSSIBLE</h2>
  <p class="abs">We are a Micro-brewery in the basement of Marlow Vale. Arthur and Ned brew most Mondays or Tuesdays... Vale Porter, Captain Alf and Last Over, 3 exceptional beers..</p>
  <div class="abs mug" role="img" aria-label="Hand raising a tall glass mug of golden beer"></div>
</section>

<section class="abs news">
  <article class="abs card" style="left:93px;top:122px;width:316px;height:424px">
    <div class="photo" role="img" aria-label="Dim brewery basement with a ladder" style="background:linear-gradient(135deg,#2b1e12,#5a3f22 55%,#1b130c)"></div>
    <p style="margin-top:22px">Our tiny little brewrig will become the brewlab soon, making way for the beast. Exciting times, made another porter last night, now experimenting with kegging methods..... all in good time. Happy Wednesday everyone.</p>
    <div class="meta"><span>16 <svg width="11" height="10" viewBox="0 0 11 10"><path d="M5.5 9.5 1 5a2.5 2.5 0 0 1 4.5-3.5A2.5 2.5 0 0 1 10 5z" fill="#fff"/></svg></span><span>0 <svg width="11" height="10" viewBox="0 0 11 10"><path d="M1 1h9v6H4l-3 2.5z" fill="#fff"/></svg></span><span>03 <svg width="11" height="10" viewBox="0 0 11 10"><circle cx="2" cy="5" r="1.6" fill="#fff"/><circle cx="9" cy="1.8" r="1.6" fill="#fff"/><circle cx="9" cy="8.2" r="1.6" fill="#fff"/><path d="M2 5 9 1.8M2 5l7 3.2" stroke="#fff"/></svg></span></div>
  </article>

  <div class="abs brand-block"><div class="name">MARLOW<br>VALE<br>BREWERY</div></div>
  <div class="abs brand-mono brandmark">MVB</div>

  <article class="abs card" style="left:776px;top:122px;width:319px;height:443px">
    <div class="photo" role="img" aria-label="Glass of dark porter with a creamy head" style="background:radial-gradient(ellipse at 50% 35%,#d7c3a1,#5a4330 45%,#1a1410 70%,#3a5a78)"></div>
    <h3>EVERY SATURDAY NIGHTS</h3>
    <p>We are often asked how we brewed such a great Porter, what's the secret..... don't tell anyone, but here is it, are you ready? ...... 2.5 years of trial and error.</p>
    <div class="meta" style="height:53px"><span>16 <svg width="11" height="10" viewBox="0 0 11 10"><path d="M5.5 9.5 1 5a2.5 2.5 0 0 1 4.5-3.5A2.5 2.5 0 0 1 10 5z" fill="#fff"/></svg></span><span>0 <svg width="11" height="10" viewBox="0 0 11 10"><path d="M1 1h9v6H4l-3 2.5z" fill="#fff"/></svg></span><span>03 <svg width="11" height="10" viewBox="0 0 11 10"><circle cx="2" cy="5" r="1.6" fill="#fff"/><circle cx="9" cy="1.8" r="1.6" fill="#fff"/><circle cx="9" cy="8.2" r="1.6" fill="#fff"/><path d="M2 5 9 1.8M2 5l7 3.2" stroke="#fff"/></svg></span></div>
  </article>
</section>

<div class="abs can-strip" role="img" aria-label="Row of navy beer cans seen from the side"></div>
<div class="abs tabs">
  <div class="on">Harbour<br>Shooter</div>
  <div>Vale<br>Porter</div>
  <div>Captain Alf</div>
  <div>The Baron</div>
</div>

<section class="abs contact">
  <div class="abs glass" role="img" aria-label="Splashing glass of spirit with ice on black"></div>
  <div class="abs portrait" role="img" aria-label="Monochrome portrait of a woman"></div>
  <h2 class="abs script">COntact Us</h2>
  <div class="abs info">Our Contact Information<br>+44 7700 900412</div>
  <div class="abs ring" style="left:512px;top:263px"><svg width="26" height="26" viewBox="0 0 24 24"><path d="M6.6 10.8a15 15 0 0 0 6.6 6.6l2.2-2.2a1 1 0 0 1 1-.25 11.4 11.4 0 0 0 3.6.57 1 1 0 0 1 1 1V20a1 1 0 0 1-1 1A17 17 0 0 1 3 4a1 1 0 0 1 1-1h3.5a1 1 0 0 1 1 1c0 1.25.2 2.45.57 3.57a1 1 0 0 1-.25 1z" fill="#fff"/></svg></div>
  <div class="abs ring" style="left:605px;top:263px"><svg width="26" height="26" viewBox="0 0 24 24"><path d="M5 2v20" stroke="#fff" stroke-width="2"/><path d="M6 3h13l-3 5 3 5H6z" fill="#fff"/></svg></div>
  <div class="abs addr">Ashbury,<br>Wessex, United Kingdom</div>
</section>

<section class="abs gallery">
  <div role="img" aria-label="Woman holding a glass of whisky" style="background:linear-gradient(135deg,#3a2418,#8a5a3c)"></div>
  <div role="img" aria-label="Glasses of whisky on ice" style="background:linear-gradient(135deg,#5a3010,#b9732a)"></div>
  <div role="img" aria-label="Bartender pouring a cocktail" style="background:linear-gradient(135deg,#1c1410,#6b4a2a)"></div>
  <div role="img" aria-label="Woman drinking from a bottle" style="background:linear-gradient(135deg,#7a6a5e,#d9cfc6)"></div>
  <div role="img" aria-label="Barrel and crystal decanter" style="background:linear-gradient(135deg,#4a2e1a,#a87a4e)"></div>
</section>

<section class="abs updates">
  <div class="abs script kick">Get Updates</div>
  <h2 class="abs">Stay In Touch With Updates</h2>
  <div class="abs field"></div>
  <div class="abs subscribe">SUBSCRIBE</div>
</section>

<footer class="abs footer" role="img" aria-label="Dark background of wooden barrels">
  <div class="abs footer-logo"><span class="brandmark">MVB</span></div>
  <div class="abs col" style="left:107px"><h4>Call us</h4><p>+44 7700 900412</p></div>
  <div class="abs col" style="left:420px"><h4>Address</h4><p>Ashbury, Wessex, United<br>Kingdom</p></div>
  <div class="abs col" style="left:760px"><h4>Email</h4><p>hello@mvbrew.co.uk</p></div>
  <div class="abs social" style="left:505px"></div>
  <div class="abs social" style="left:577px"></div>
  <div class="abs social" style="left:651px"></div>
</footer>

</body>
</html>
```